Industrial Automation company requires a business card design

Valtrin Automation provides design & build of Automated Equipment for manufacturing industry.
www.valtrinautomation.example
The equipment we design is used for manufacturing in sectors such as medical device, pharmaceutical, aerospace and electronics.
We require a new business card design which incorporates our (New) logo and the key message words:
Automated Equipment:
Design, Build, Control, Test, Support

```html
<!DOCTYPE html>
<html lang="en">
<head>
<meta charset="utf-8">
<title>Valtrin Automation – Business Card</title>
<link rel="stylesheet" href="https://fonts.googleapis.com/css2?family=Open+Sans:wght@400;600;700&display=swap">
<style>
  :root {
    --backdrop: #e9e6e3;
    --card-light: #f7f5f4;
    --card-dark: #2a2828;
    --brand-green: #1f8a3b;
    --ink: #2b2b2b;
  }
  * { margin: 0; padding: 0; box-sizing: border-box; }
  html, body { width: 1200px; height: 900px; overflow: hidden; }
  body {
    background: var(--backdrop);
    font-family: "Open Sans", Arial, sans-serif;
    position: relative;
  }
  .card {
    position: absolute;
    box-shadow: 0 4px 14px rgba(0,0,0,0.18);
  }
  .card--front {
    left: 238px; top: 62px; width: 555px; height: 342px;
    background: var(--card-light);
  }
  .card--back {
    left: 457px; top: 518px; width: 560px; height: 343px;
    background: var(--card-dark);
  }
  .holder { position: absolute; left: 37px; top: 36px; }
  .holder__name {
    color: var(--brand-green);
    font-weight: 600;
    font-size: 17px;
    line-height: 22px;
  }
  .holder__title {
    color: var(--ink);
    font-size: 14px;
    line-height: 18px;
  }
  .wordmark {
    position: absolute;
    left: 0; right: 0;
    display: flex;
    flex-direction: column;
    align-items: center;
    color: var(--brand-green);
    font-weight: 700;
    text-align: center;
  }
  .wordmark__dot {
    border-radius: 50%;
    background: var(--brand-green);
  }
  .card--front .wordmark { top: 88px; }
  .card--front .wordmark__dot { width: 40px; height: 40px; margin-bottom: 16px; }
  .card--front .wordmark__name { font-size: 26px; letter-spacing: 2px; line-height: 32px; }
  .card--back .wordmark { top: 92px; }
  .card--back .wordmark__dot { width: 58px; height: 58px; margin-bottom: 22px; }
  .card--back .wordmark__name { font-size: 34px; letter-spacing: 3px; line-height: 42px; }
  .contact {
    position: absolute;
    left: 177px; top: 230px;
    list-style: none;
    color: var(--ink);
    font-size: 15px;
  }
  .contact__item {
    display: flex;
    align-items: center;
    height: 20.5px;
  }
  .contact__icon {
    width: 12px; height: 12px;
    margin-right: 9px;
    fill: var(--brand-green);
  }
</style>
</head>
<body>
  <section class="card card--front" aria-label="Business card front">
    <div class="holder">
      <p class="holder__name">DANIEL MARSH</p>
      <p class="holder__title">Director Operations</p>
    </div>
    <div class="wordmark">
      <span class="wordmark__dot"></span>
      <span class="wordmark__name">VALTRIN AUTOMATION</span>
    </div>
    <ul class="contact">
      <li class="contact__item">
        <svg class="contact__icon" viewBox="0 0 12 12" aria-hidden="true"><path d="M3 0h6a1 1 0 0 1 1 1v10a1 1 0 0 1-1 1H3a1 1 0 0 1-1-1V1a1 1 0 0 1 1-1zm0.8 1.5v7.5h4.4V1.5zM6 9.8a0.7 0.7 0 1 0 0 1.4a0.7 0.7 0 0 0 0-1.4z"/></svg>
        +61 400 555 019
      </li>
      <li class="contact__item">
        <svg class="contact__icon" viewBox="0 0 12 12" aria-hidden="true"><path d="M0 2.5h12v7H0zM0.8 3.2L6 6.8l5.2-3.6v-0.1H0.8z"/></svg>
        d.marsh@valtrinautomation.example
      </li>
      <li class="contact__item">
        <svg class="contact__icon" viewBox="0 0 12 12" aria-hidden="true"><path d="M6 0a6 6 0 1 0 0 12A6 6 0 0 0 6 0zm-1 2.2c1 .3 1.6 1 1.3 1.7c-.4.8-1.6.6-1.8 1.6c-.2.9 1 1.2.7 2.2c-.2.8-1.3 1-2 .6A4.5 4.5 0 0 1 5 2.2zm3.2 1.2c.8.4 1.4 1.5 1.3 2.8c-.6.1-1.2-.4-1.7-.1c-.6.4-.1 1.3-.8 1.6c-.6.3-1.1-.4-1-1.1c.2-.9 1.3-.9 1.4-1.8c.1-.6-.4-1 .8-1.4z"/></svg>
        www.valtrinautomation.example
      </li>
    </ul>
  </section>

  <section class="card card--back" aria-label="Business card back">
    <div class="wordmark">
      <span class="wordmark__dot"></span>
      <span class="wordmark__name">VALTRIN AUTOMATION</span>
    </div>
  </section>
</body>
</html>
```